Texas Civic Builders Summit Needs a Flyer

One-page event graphic/flyer and header needed. Logos provided.

2023 Texas Civic Builders Summit
Bold Ventures – True Accounts, True Answers, True Wins
August 10-11, 2023
San Antonio, Texas

About the Forum:
“Capital projects are full of risk. It’s not a question of eliminating risk, it’s a question of how to clearly identify it, reduce it, change it, or battle it.”
- Denise Holmgarten, Founder, U-BraMQ; San Antonio City Architect (retired)

Real Stories, Real Solutions, Real Success: U-BraMQ’s Texas Civic Builders Summit (TCBS) is designed to help you attain project success by hearing from Public Project Owners, architects, engineers, consultants, contractors, and suppliers. We are all in this together, and U-BraMQ is the organization that champions cross-collaboration and communication for project success!

For reference in design ONLY -
Here are some topic areas that bring project risks and/or rewards and that ultimately affect the Public Project Owner’s project success:

• Project Planning
• Regional Growth Shifts
• Project Funding
• Contracting
• Governmental Regulations
• Long-term COVID Impacts
• Infrastructure and Site Design
• Safety and Security
• Sustainability and Resilience
• Construction Predictability
• Leveraging Technology
• Facility Operations

Target Market(s)

Architects, Engineers, Contractors, project owners

Industry/Entity Type

Design and Construction

Requirements
Must have
• This is for a one-page (8.5x11) event graphic/flyer only - logos are provided. U-BraMQ logo, Texas Civic Builders Summit (TCBS) logo, 2023 Texas Civic Builders Summit, date, location
Nice to have
• Graphic(s) that represent the design and construction industry and the theme of this event (title, topics covered)
Should not have
• Full project description

```html
<!DOCTYPE html>
<html lang="en">
<head>
<meta charset="utf-8">
<title>2023 Texas Civic Builders Summit – Flyer and Web Banner</title>
<link rel="stylesheet" href="https://fonts.googleapis.com/css2?family=Anton&family=Poppins:wght@400;500;600;700&display=swap">
<style>
  :root {
    --blue: #1f3f9e;
    --blue-dark: #1a3388;
    --green: #7cb342;
    --ink: #222226;
    --charcoal: #2b2b2d;
    --white: #ffffff;
    --page: #efefef;
    --sky-top: #9fb3d3;
    --sky-mid: #c3cedd;
    --city: #8c8f92;
    --harbor: #4d5660;
  }
  * { box-sizing: border-box; margin: 0; padding: 0; }
  html, body { width: 783px; height: 1200px; overflow: hidden; }
  body { background: var(--page); font-family: "Poppins", sans-serif; color: var(--ink); position: relative; }

  /* ---------- Flyer ---------- */
  .flyer {
    position: absolute; left: 91px; top: 40px;
    width: 600px; height: 776px; background: var(--white);
    overflow: hidden; box-shadow: 0 4px 14px rgba(0,0,0,.18);
  }
  .flyer-hero { position: absolute; left: 0; top: 0; width: 600px; height: 400px; display: block; }
  .flyer-brand {
    position: absolute; left: 34px; top: 44px; width: 210px;
    display: flex; align-items: center; gap: 9px;
  }
  .brand-dot { width: 22px; height: 22px; border-radius: 50%; background: var(--blue); flex: none; }
  .brand-name { font-weight: 600; color: var(--blue); font-size: 19px; line-height: 1.12; }

  .flyer-title { position: absolute; left: 0; top: 376px; width: 100%; text-align: center; font-family: "Anton", sans-serif; line-height: 1.02; }
  .flyer-title .year { display: block; color: var(--blue); font-size: 60px; }
  .flyer-title .name { display: block; color: var(--green); font-size: 49px; }

  .tagline-pill {
    position: absolute; left: 53px; top: 503px; width: 494px; height: 30px;
    background: var(--blue); border-radius: 15px; color: var(--white);
    font-weight: 600; font-size: 12px; letter-spacing: .1px;
    display: flex; align-items: center; justify-content: center;
  }

  .event-info { position: absolute; left: 33px; top: 547px; width: 300px; }
  .event-date { display: flex; align-items: center; gap: 7px; font-size: 27px; font-weight: 700; line-height: 1.1; }
  .event-date .days { color: var(--blue); }
  .event-date .yr { font-weight: 400; }
  .event-place { display: flex; align-items: center; gap: 9px; font-size: 18px; font-weight: 700; margin-top: 5px; padding-left: 1px; }
  .about-heading { font-size: 13.5px; font-weight: 700; margin-top: 10px; }
  .about-heading span { color: var(--blue); }
  .about-list { list-style: none; margin-top: 8px; }
  .about-list li { position: relative; padding-left: 14px; font-size: 8.2px; line-height: 1.3; margin-bottom: 10px; width: 270px; }
  .about-list li::before {
    content: ""; position: absolute; left: 0; top: 2px; width: 7px; height: 7px;
    border-radius: 50%; background: var(--blue);
  }

  .summit-about { position: absolute; left: 355px; top: 553px; width: 220px; }
  .summit-about h3 { font-size: 8.4px; font-weight: 700; color: var(--blue); }
  .summit-about p { font-size: 7.7px; line-height: 1.35; text-align: justify; margin-top: 6px; }
  .org-mark { display: flex; align-items: center; gap: 8px; margin-top: 14px; margin-left: 8px; }
  .org-dot { width: 34px; height: 34px; border-radius: 50%; background: var(--blue); }
  .org-name { font-size: 30px; font-weight: 500; color: var(--blue); line-height: 1; }

  .flyer-footer { position: absolute; left: 0; bottom: 0; width: 600px; height: 56px; background: var(--charcoal); }
  .call-now {
    position: absolute; left: 0; top: 0; width: 300px; height: 56px; background: var(--green);
    border-radius: 0 28px 28px 0; color: var(--white); font-weight: 700; font-size: 17px;
    display: flex; align-items: center; padding-left: 33px;
  }
  .web-link {
    position: absolute; left: 320px; top: 0; height: 56px; color: var(--white);
    font-weight: 600; font-size: 14px; display: flex; align-items: center; gap: 8px; letter-spacing: .3px;
  }

  /* ---------- Web banner ---------- */
  .banner {
    position: absolute; left: 91px; top: 856px; width: 600px; height: 249px;
    background: var(--white); overflow: hidden; box-shadow: 0 4px 14px rgba(0,0,0,.18);
  }
  .banner-art { position: absolute; left: 0; top: 0; width: 600px; height: 249px; display: block; }
  .banner-brand { position: absolute; left: 18px; top: 32px; width: 128px; display: flex; align-items: center; gap: 6px; }
  .banner-brand .brand-dot { width: 14px; height: 14px; }
  .banner-brand .brand-name { font-size: 12.5px; }
  .banner-title { position: absolute; left: 154px; top: 26px; font-family: "Anton", sans-serif; line-height: 1.05; }
  .banner-title .year { display: block; color: var(--blue); font-size: 34px; }
  .banner-title .name { display: block; color: var(--green); font-size: 16.5px; }

  .banner-theme { position: absolute; left: 22px; top: 111px; height: 38px; display: flex; align-items: center; gap: 9px; }
  .theme-word { font-family: "Anton", sans-serif; color: var(--blue); font-size: 19px; line-height: .9; }
  .theme-word small { display: block; font-family: "Poppins", sans-serif; font-weight: 700; color: var(--ink); font-size: 10px; line-height: 1.1; }
  .theme-rule { width: 2px; height: 30px; background: var(--white); }
  .theme-points { display: grid; grid-template-columns: auto auto; column-gap: 10px; row-gap: 2px; list-style: none; }
  .theme-points li { color: var(--white); font-size: 10px; font-weight: 600; display: flex; align-items: center; gap: 4px; }
  .tick { width: 9px; height: 9px; border-radius: 50%; background: var(--blue); flex: none; }

  .banner-date { position: absolute; left: 22px; top: 152px; height: 34px; display: flex; align-items: center; gap: 6px; color: var(--white); font-size: 22px; font-weight: 700; }
  .banner-date .days { color: var(--green); }
  .banner-date .yr { font-weight: 400; }
  .banner-place { position: absolute; left: 22px; top: 196px; height: 36px; display: flex; align-items: center; gap: 7px; font-size: 19px; font-weight: 700; }
  .banner-org { position: absolute; left: 298px; top: 204px; display: flex; align-items: center; gap: 5px; }
  .banner-org .org-dot { width: 17px; height: 17px; }
  .banner-org .org-name { font-size: 15px; }
</style>
</head>
<body>

<main class="flyer">
  <svg class="flyer-hero" viewBox="0 0 600 400" aria-hidden="false">
    <defs>
      <linearGradient id="cityTones" x1="0" y1="0" x2="0" y2="1">
        <stop offset="0" stop-color="#9fb3d3"/>
        <stop offset=".35" stop-color="#c3cedd"/>
        <stop offset=".65" stop-color="#8c8f92"/>
        <stop offset="1" stop-color="#4d5660"/>
      </linearGradient>
    </defs>
    <rect role="img" aria-label="Photo of a downtown skyline with a high-rise under construction and tower cranes by the harbor" x="0" y="0" width="600" height="400" fill="url(#cityTones)"/>
    <path d="M0 0 H345 C320 98 235 142 150 142 C260 128 310 80 327 0 Z" fill="#1f3f9e"/>
    <path d="M0 0 H327 C305 85 230 132 130 134 C75 135 35 128 0 118 Z" fill="#ffffff"/>
    <path d="M0 385 Q300 320 600 385 V400 H0 Z" fill="#7cb342"/>
    <path d="M0 398 Q300 340 600 395 V400 H0 Z" fill="#ffffff"/>
  </svg>

  <div class="flyer-brand">
    <span class="brand-dot"></span>
    <span class="brand-name">Texas Civic Builders Summit</span>
  </div>

  <h1 class="flyer-title">
    <span class="year">2023 TEXAS</span>
    <span class="name">CIVIC BUILDERS SUMMIT</span>
  </h1>

  <div class="tagline-pill">BOLD VENTURES – TRUE ACCOUNTS, TRUE ANSWERS, TRUE WINS</div>

  <section class="event-info">
    <p class="event-date">
      <svg width="22" height="22" viewBox="0 0 22 22" aria-hidden="true"><rect x="2" y="4" width="18" height="16" rx="2" fill="none" stroke="#222226" stroke-width="2.2"/><rect x="2" y="4" width="18" height="5" fill="#222226"/><rect x="6" y="1" width="2.4" height="5" fill="#222226"/><rect x="13.6" y="1" width="2.4" height="5" fill="#222226"/><g fill="#222226"><rect x="5" y="11" width="3" height="2.5"/><rect x="9.5" y="11" width="3" height="2.5"/><rect x="14" y="11" width="3" height="2.5"/><rect x="5" y="15" width="3" height="2.5"/><rect x="9.5" y="15" width="3" height="2.5"/><rect x="14" y="15" width="3" height="2.5"/></g></svg>
      <span>AUGUST <span class="days">10–11,</span> <span class="yr">2023</span></span>
    </p>
    <p class="event-place">
      <svg width="15" height="20" viewBox="0 0 15 20" aria-hidden="true"><path d="M7.5 0C3.4 0 0 3.3 0 7.4 0 12.8 7.5 20 7.5 20S15 12.8 15 7.4C15 3.3 11.6 0 7.5 0Z" fill="#1f3f9e"/><circle cx="7.5" cy="7.3" r="2.8" fill="#fff"/></svg>
      SAN ANTONIO, TEXAS
    </p>
    <h2 class="about-heading"><span>ABOUT</span> THE FORUM</h2>
    <ul class="about-list">
      <li>Capital projects are full of risk. It’s not a question of eliminating risk, it’s a question of how to clearly identify it, reduce it, change it, or battle it.</li>
      <li>Denise Holmgarten, Founder, U-BraMQ; San Antonio City Architect (retired)</li>
    </ul>
  </section>

  <section class="summit-about">
    <h3>REAL STORIES, REAL SOLUTIONS, REAL SUCCESS:</h3>
    <p>U-BraMQ’s Texas Civic Builders Summit (TCBS) is designed to help you attain project success by hearing from Public Project Owners, architects, engineers, consultants, contractors, and suppliers. We are all in this together, and U-BraMQ is the organization that champions cross-collaboration and communication for project success!</p>
    <div class="org-mark">
      <span class="org-dot"></span>
      <span class="org-name">U-BraMQ</span>
    </div>
  </section>

  <footer class="flyer-footer">
    <div class="call-now">CALL US NOW: (512)555-0148</div>
    <div class="web-link">
      <svg width="14" height="14" viewBox="0 0 14 14" aria-hidden="true"><g fill="none" stroke="#7cb342" stroke-width="1.2"><circle cx="7" cy="7" r="6"/><ellipse cx="7" cy="7" rx="2.6" ry="6"/><path d="M1 7H13M2 4H12M2 10H12"/></g></svg>
      WWW.u-bramq-events.org
    </div>
  </footer>
</main>

<section class="banner">
  <svg class="banner-art" viewBox="0 0 600 249" aria-hidden="false">
    <defs>
      <linearGradient id="siteTones" x1="0" y1="0" x2="0" y2="1">
        <stop offset="0" stop-color="#b9cbe3"/>
        <stop offset=".5" stop-color="#a9a79c"/>
        <stop offset="1" stop-color="#5d7455"/>
      </linearGradient>
    </defs>
    <rect role="img" aria-label="Photo of a bridge tower under construction with a crane beside a river city" x="330" y="0" width="270" height="249" fill="url(#siteTones)"/>
    <path d="M0 0 H343 V140 L408 178 C428 200 436 228 446 249 H0 Z" fill="#ffffff"/>
    <path d="M408 178 C428 200 436 228 446 249" fill="none" stroke="#1f3f9e" stroke-width="4"/>
    <rect x="341" y="0" width="4" height="106" fill="#1f3f9e"/>
    <path d="M0 105 H300 L330 150 H0 Z" fill="#7cb342"/>
    <path d="M0 150 H398 L408 186 H0 Z" fill="#1f3f9e"/>
  </svg>

  <div class="banner-brand">
    <span class="brand-dot"></span>
    <span class="brand-name">Texas Civic Builders Summit</span>
  </div>
  <h2 class="banner-title">
    <span class="year">2023 TEXAS</span>
    <span class="name">CIVIC BUILDERS SUMMIT</span>
  </h2>

  <div class="banner-theme">
    <p class="theme-word">BOLD<small>VENTURES</small></p>
    <span class="theme-rule"></span>
    <ul class="theme-points">
      <li><span class="tick"></span>True Accounts</li>
      <li><span class="tick"></span>True Answers</li>
      <li><span class="tick"></span>True Wins</li>
    </ul>
  </div>

  <p class="banner-date">
    <svg width="17" height="17" viewBox="0 0 22 22" aria-hidden="true"><rect x="2" y="4" width="18" height="16" rx="2" fill="none" stroke="#7cb342" stroke-width="2.2"/><rect x="2" y="4" width="18" height="5" fill="#7cb342"/><g fill="#7cb342"><rect x="5" y="11" width="3" height="2.5"/><rect x="9.5" y="11" width="3" height="2.5"/><rect x="14" y="11" width="3" height="2.5"/><rect x="5" y="15" width="3" height="2.5"/><rect x="9.5" y="15" width="3" height="2.5"/></g></svg>
    <span>AUGUST <span class="days">10–11,</span> <span class="yr">2023</span></span>
  </p>
  <p class="banner-place">
    <svg width="13" height="18" viewBox="0 0 15 20" aria-hidden="true"><path d="M7.5 0C3.4 0 0 3.3 0 7.4 0 12.8 7.5 20 7.5 20S15 12.8 15 7.4C15 3.3 11.6 0 7.5 0Z" fill="#1f3f9e"/><circle cx="7.5" cy="7.3" r="2.8" fill="#fff"/></svg>
    SAN ANTONIO, TEXAS
  </p>
  <div class="banner-org">
    <span class="org-dot"></span>
    <span class="org-name">U-BraMQ</span>
  </div>
</section>

</body>
</html>
```